Orvel Crest Holdings Ltd
Creative Brief
Dara Kolby
COO
27B Hollin Row, London, E3 9TQ
dk@orvelcrest.co.uk
27b Hollin Row
Just the logo and the company's name on the green background

```html
<!DOCTYPE html>
<html lang="en">
<head>
<meta charset="utf-8">
<title>Orvel Crest Holdings Ltd – Business Card</title>
<link rel="stylesheet" href="https://fonts.googleapis.com/css2?family=Cormorant+Garamond:wght@500&family=Montserrat:wght@400;500;700&display=swap">
<style>
  :root {
    --page-bg: #e8e8e9;
    --gold-light: #e0c999;
    --gold-mid: #d2b681;
    --gold-dark: #c4a56e;
    --gold-text: #d4b26a;
    --forest: #3e4030;
    --cream: #f6f1e6;
    --white: #ffffff;
  }
  * { margin: 0; padding: 0; box-sizing: border-box; }
  html, body { width: 1200px; height: 901px; overflow: hidden; }
  body {
    position: relative;
    background: var(--page-bg);
    font-family: "Montserrat", Arial, sans-serif;
  }
  .card { position: absolute; border-radius: 24px; overflow: hidden; }

  /* Front */
  .card-front {
    left: 416px; top: 134px; width: 489px; height: 309px;
    background: linear-gradient(120deg, var(--gold-light) 0%, var(--gold-mid) 50%, var(--gold-dark) 100%);
  }
  .card-front .mark-circle { position: absolute; left: 199px; top: 36px; }
  .card-front .brand-name {
    position: absolute; left: 0; width: 100%; top: 152px;
    text-align: center; color: var(--white);
    font-family: "Cormorant Garamond", Georgia, serif; font-weight: 500;
    font-size: 40px; line-height: 1; letter-spacing: 1px;
  }
  .card-front .brand-sub {
    position: absolute; left: 0; width: 100%; top: 201px;
    text-align: center; color: var(--white);
    font-family: "Cormorant Garamond", Georgia, serif; font-weight: 500;
    font-size: 14px; letter-spacing: 1px;
  }

  /* Back */
  .card-back {
    left: 297px; top: 482px; width: 608px; height: 382px;
    background: var(--forest);
  }
  .card-back .mark-circle { position: absolute; left: 448px; top: 30px; }
  .card-back .brand-name {
    position: absolute; left: 380px; width: 234px; top: 144px;
    text-align: center; color: var(--cream);
    font-family: "Cormorant Garamond", Georgia, serif; font-weight: 500;
    font-size: 30px; line-height: 1;
  }
  .card-back .brand-sub {
    position: absolute; left: 380px; width: 234px; top: 184px;
    text-align: center; color: var(--cream);
    font-family: "Cormorant Garamond", Georgia, serif; font-weight: 500;
    font-size: 12.5px; letter-spacing: .5px;
  }
  .person {
    position: absolute; left: 14px; top: 170px;
    border-left: 3px solid var(--gold-text); padding-left: 17px;
  }
  .person-name {
    color: var(--gold-text); font-weight: 700; font-size: 23px; line-height: 1.1;
  }
  .person-role { color: var(--white); font-size: 12px; margin-top: 4px; }
  .contacts { position: absolute; left: 26px; top: 258px; list-style: none; }
  .contacts li {
    display: flex; align-items: center; gap: 10px;
    color: var(--white); font-size: 12px; height: 19.5px;
  }
  .contacts svg { width: 9px; height: 9px; fill: var(--gold-text); }
  .address {
    position: absolute; right: 46px; top: 289px;
    text-align: right; color: var(--white); font-size: 12px; line-height: 22px;
  }
  .address-pin { position: absolute; right: 26px; top: 298px; }
</style>
</head>
<body>

<section class="card card-front" aria-label="Card front">
  <svg class="mark-circle" width="92" height="92" viewBox="0 0 92 92" aria-hidden="true">
    <circle cx="46" cy="46" r="44" fill="none" stroke="var(--white)" stroke-width="2.5"/>
  </svg>
  <div class="brand-name">ORVEL CREST</div>
  <div class="brand-sub">HOLDINGS LTD</div>
</section>

<section class="card card-back" aria-label="Card back">
  <svg class="mark-circle" width="96" height="96" viewBox="0 0 96 96" aria-hidden="true">
    <circle cx="48" cy="48" r="46" fill="none" stroke="var(--gold-text)" stroke-width="2.5"/>
  </svg>
  <div class="brand-name">ORVEL CREST</div>
  <div class="brand-sub">HOLDINGS LTD</div>

  <div class="person">
    <div class="person-name">DARA KOLBY</div>
    <div class="person-role">COO</div>
  </div>

  <ul class="contacts">
    <li>
      <svg viewBox="0 0 10 10"><path d="M2 0.5 L3.8 2.6 L2.9 3.8 C3.5 5 4.9 6.4 6.2 7.1 L7.4 6.2 L9.5 8 L8.4 9.5 C4.5 9.2 0.8 5.5 0.5 1.6 Z"/></svg>
      +44 (0)20 7946 0321
    </li>
    <li>
      <svg viewBox="0 0 10 10"><path d="M2.5 0 H7.5 V10 H2.5 Z M3.3 1 V8 H6.7 V1 Z"/></svg>
      +44 (0)77 0090 0482
    </li>
    <li>
      <svg viewBox="0 0 10 10"><path d="M0 2 H10 V8.5 H0 Z M0.8 2.6 L5 5.6 L9.2 2.6 V2.3 H0.8 Z" fill-rule="evenodd"/></svg>
      dk@orvelcrest.co.uk
    </li>
    <li>
      <svg viewBox="0 0 10 10"><path d="M5 0 C2.6 0 1.2 1.7 1.2 3.6 C1.2 6.2 5 10 5 10 C5 10 8.8 6.2 8.8 3.6 C8.8 1.7 7.4 0 5 0 Z M5 2.2 A1.4 1.4 0 1 1 5 5 A1.4 1.4 0 1 1 5 2.2 Z" fill-rule="evenodd"/></svg>
      27b Hollin Row
    </li>
  </ul>

  <div class="address">27B Hollin Row<br>London, E3 9TQ</div>
  <svg class="address-pin" width="14" height="19" viewBox="0 0 10 13" aria-hidden="true">
    <path d="M5 0 C2.3 0 0.5 2 0.5 4.4 C0.5 7.6 5 13 5 13 C5 13 9.5 7.6 9.5 4.4 C9.5 2 7.7 0 5 0 Z M5 2.6 A1.8 1.8 0 1 1 5 6.2 A1.8 1.8 0 1 1 5 2.6 Z" fill="var(--gold-text)" fill-rule="evenodd"/>
  </svg>
</section>

</body>
</html>
```